Business cards, letterheads, envelopes, notepad design

We are a new business in Miami, Florida. We produce business printing, signs and photogifts such as canvas prints, t shirts, mugs, phone cases etc.
Our store will be very modern with interactive stations for clients to design their own products on our cloud design software. We want something that will appeal to business clients and the general public clients.
We need designs for business cards, letterheads, notepads, and envelopes - all 4 colour process - full bleed OK.

Target Market(s)

We target both business clients and the general public.

Industry/Entity Type

Store

Font styles to use
Sans Serif
Other font styles liked:
• Harabara

Colors
acd036
33a6d7
e34197
000000

Requirements
Must have
• Cyan, Magenta, Lime Green
Should not have
• No cats. Absolutely.

```html
<!DOCTYPE html>
<html lang="en">
<head>
<meta charset="utf-8">
<title>PrintNest Business Cards</title>
<link href="https://fonts.googleapis.com/css2?family=Nunito:wght@700;800&family=Open+Sans:wght@400;600;700&display=swap" rel="stylesheet">
<style>
  :root{
    --lime:#acd036;
    --cyan:#33a6d7;
    --magenta:#e34197;
    --black:#000000;
    --card-black:#0b0b0b;
    --white:#ffffff;
    --stage:#e9e6e1;
  }
  *{margin:0;padding:0;box-sizing:border-box}
  html,body{width:1200px;height:1024px;overflow:hidden}
  body{
    background:var(--stage);
    display:flex;flex-direction:column;align-items:center;justify-content:center;gap:70px;
    font-family:"Open Sans",Arial,sans-serif;
  }
  .card{
    width:700px;height:400px;position:relative;overflow:hidden;
    box-shadow:0 10px 28px rgba(0,0,0,.22);
  }
  .wordmark{
    font-family:"Nunito",Arial,sans-serif;font-weight:800;
    font-size:78px;letter-spacing:-1px;line-height:1;
    display:flex;align-items:center;gap:18px;
  }
  .wordmark .mark-square{width:30px;height:30px;background:var(--cyan);flex:none}

  /* Front */
  .card-front{background:var(--white)}
  .front-top{
    position:absolute;left:0;top:0;width:100%;height:216px;
    display:flex;align-items:center;justify-content:center;
  }
  .card-front .wordmark{color:var(--black)}
  .color-rule{
    position:absolute;left:0;top:216px;width:100%;height:8px;display:flex;
  }
  .color-rule span{flex:1}
  .lime{background:var(--lime)}
  .cyan{background:var(--cyan)}
  .magenta{background:var(--magenta)}
  .front-bottom{
    position:absolute;left:0;top:224px;width:100%;bottom:0;background:var(--card-black);
    display:flex;justify-content:space-between;align-items:center;padding:0 44px;
    color:var(--white);
  }
  .person .name{color:var(--magenta);font-weight:700;font-size:22px;letter-spacing:.5px}
  .person .role{color:var(--cyan);font-size:18px;margin-top:2px}
  .person .address{font-size:17px;line-height:1.35;margin-top:4px}
  .contacts{list-style:none;font-size:16px;line-height:1.6}
  .contacts li{display:flex;align-items:center;gap:10px}
  .contacts svg{width:16px;height:16px;flex:none}

  /* Back */
  .card-back{background:var(--card-black)}
  .back-center{
    position:absolute;left:0;top:0;width:100%;height:360px;
    display:flex;align-items:center;justify-content:center;
  }
  .card-back .wordmark{color:var(--white);font-size:96px}
  .card-back .wordmark .mark-square{width:36px;height:36px}
  .edge-band{position:absolute;left:0;bottom:0;width:100%;height:40px;display:flex}
  .edge-band span{flex:1}
</style>
</head>
<body>

<section class="card card-front" aria-label="Business card front">
  <div class="front-top">
    <div class="wordmark"><span class="mark-square"></span>PrintNest</div>
  </div>
  <div class="color-rule"><span class="lime"></span><span class="cyan"></span><span class="magenta"></span></div>
  <div class="front-bottom">
    <div class="person">
      <p class="name">MARCUS VALE</p>
      <p class="role">Job Title</p>
      <p class="address">Address Line 1,<br>State, Zip Code, Country Name</p>
    </div>
    <ul class="contacts">
      <li>
        <svg viewBox="0 0 16 16"><path d="M4 1.5l2.5 3-1.5 1.5c.8 2 2.5 3.7 4.5 4.5L11 9l3 2.5-1.5 2.5C7 14 2 9 2 3z" fill="var(--lime)"/></svg>
        305-555-01847
      </li>
      <li>
        <svg viewBox="0 0 16 16"><rect x="4" y="1" width="8" height="14" rx="1.5" fill="var(--lime)"/><rect x="5.5" y="3" width="5" height="8" fill="var(--card-black)"/></svg>
        305-555-0192
      </li>
      <li>
        <svg viewBox="0 0 16 16"><rect x="1" y="3" width="14" height="10" fill="var(--lime)"/><path d="M1 3l7 6 7-6" fill="none" stroke="var(--card-black)" stroke-width="1.4"/></svg>
        hello@printnest.com
      </li>
      <li>
        <svg viewBox="0 0 16 16"><circle cx="8" cy="8" r="7" fill="var(--lime)"/><path d="M1 8h14M8 1c-3 4-3 10 0 14M8 1c3 4 3 10 0 14" fill="none" stroke="var(--card-black)" stroke-width="1"/></svg>
        www.printnest.com
      </li>
    </ul>
  </div>
</section>

<section class="card card-back" aria-label="Business card back">
  <div class="back-center">
    <div class="wordmark"><span class="mark-square"></span>PrintNest</div>
  </div>
  <div class="edge-band"><span class="lime"></span><span class="cyan"></span><span class="magenta"></span></div>
</section>

</body>
</html>
```